Dalton Power Supply, Inc. Business Card Design

We are an Electrical Distributor looking for a Modern, Professional Business Card design.

Target Market(s)

Residential Commercial Industrial

Industry/Entity Type

Electrical

Contact Information for Business Card

Dalton Power Supply, Inc.
418 Maple Ridge Lane
Brookvale, NC 27514
555-214-7630
555-214-8842 Fax
daltonpower@brightmail-example.net

```html
<!DOCTYPE html>
<html lang="en">
<head>
<meta charset="utf-8">
<title>Dalton Power Supply, Inc. — Business Card</title>
<link rel="stylesheet" href="https://fonts.googleapis.com/css2?family=Lato:wght@300;400&display=swap">
<style>
  :root {
    --backdrop: #5b5b5d;
    --card: #2b2b2c;
    --ink: #d9d9d9;
    --ink-soft: #bdbdbd;
    --rule: #e6e6e6;
  }
  * { box-sizing: border-box; margin: 0; padding: 0; }
  html, body {
    width: 1200px;
    height: 800px;
    overflow: hidden;
    background: var(--backdrop);
    font-family: "Lato", Arial, sans-serif;
  }
  .stage {
    width: 1200px;
    height: 800px;
    display: flex;
    align-items: center;
    justify-content: center;
  }
  .business-card {
    position: relative;
    width: 980px;
    height: 560px;
    background: var(--card);
    display: flex;
    box-shadow: 0 18px 40px rgba(0,0,0,0.35);
  }
  .brand-side {
    width: 40%;
    display: flex;
    align-items: center;
    justify-content: center;
    padding: 110px 30px 0;
  }
  .company-name {
    font-weight: 300;
    font-size: 34px;
    line-height: 1.15;
    letter-spacing: 0.5px;
    color: var(--ink);
    display: flex;
    align-items: center;
    gap: 22px;
  }
  .company-mark {
    flex: none;
    width: 70px;
    height: 70px;
    background: var(--ink);
  }
  .company-text {
    display: block;
    width: 200px;
  }
  .divider {
    position: absolute;
    left: 40%;
    top: 36px;
    bottom: 36px;
    width: 2px;
    background: linear-gradient(to bottom, rgba(230,230,230,0), var(--rule) 20%, var(--rule) 80%, rgba(230,230,230,0));
  }
  .contact-side {
    width: 60%;
    padding: 78px 30px 0 64px;
    color: var(--ink-soft);
    font-weight: 300;
    font-size: 26px;
    line-height: 1.35;
  }
  .contact-row {
    display: flex;
    align-items: flex-start;
    gap: 20px;
  }
  .contact-row + .contact-row { margin-top: 6px; }
  .contact-row.spaced { margin-top: 30px; }
  .contact-icon {
    width: 24px;
    height: 24px;
    flex: none;
    margin-top: 6px;
    fill: var(--ink);
  }
  .address { display: block; font-style: normal; }
</style>
</head>
<body>
<main class="stage">
  <article class="business-card">
    <section class="brand-side">
      <h1 class="company-name"><span class="company-mark"></span><span class="company-text">Dalton Power Supply, Inc.</span></h1>
    </section>
    <div class="divider"></div>
    <section class="contact-side">
      <div class="contact-row">
        <svg class="contact-icon" viewBox="0 0 24 24" aria-hidden="true">
          <path d="M3 9c0-3 4-5 9-5s9 2 9 5v2h-5V9c0-1-2-1.5-4-1.5S8 8 8 9v2H3z"/>
          <path d="M7 12h10l3 8H4z"/>
        </svg>
        <span>555-214-7630</span>
      </div>
      <div class="contact-row">
        <svg class="contact-icon" viewBox="0 0 24 24" aria-hidden="true">
          <path d="M6 3h12v6H6z"/>
          <path d="M3 10h18v8h-3v3H6v-3H3zM8 15v4h8v-4z"/>
        </svg>
        <span>555-214-8842</span>
      </div>
      <div class="contact-row spaced">
        <svg class="contact-icon" viewBox="0 0 24 24" aria-hidden="true">
          <path d="M2 5h20v14H2zM4 7v1l8 5 8-5V7l-8 5z"/>
        </svg>
        <span>daltonpower@brightmail-example.net</span>
      </div>
      <div class="contact-row">
        <svg class="contact-icon" viewBox="0 0 24 24" aria-hidden="true">
          <path d="M12 2a7 7 0 0 1 7 7c0 5-7 13-7 13S5 14 5 9a7 7 0 0 1 7-7zm0 4a3 3 0 1 0 0 6 3 3 0 0 0 0-6z"/>
        </svg>
        <address class="address">418 Maple Ridge Lane<br>Brookvale, NC 27514</address>
      </div>
    </section>
  </article>
</main>
</body>
</html>
```